Rtvlegal.com needs a wedsite. Law Office of Bernard T. Whitfield

Bernard T. Whitfield is a criminal law firm that is 5 years old. We have already had all the content written and now just need the website designed. We also just finished our logo design using Pixel Harbor and would like it used in the design of the website.

Industry/Entity Type

Law Firm

Number of Pages Required

5+ page

Requirements
Must have
• I was our new logo to be on the website also. I want Dallas sites as the stock pictures for the website. For example the Grey Stone Hall. I also need to be able to add ClipNest videos. It has to adjust to be seen on computers and also cell phones. I need to be able to have a information sheet for clients to fill out and submit back to me.

```html
<!DOCTYPE html>
<html lang="en">
<head>
<meta charset="utf-8">
<title>Law Office of Bernard T. Whitfield</title>
<link rel="stylesheet" href="https://fonts.googleapis.com/css2?family=Questrial&family=Arimo:wght@400;700&display=swap">
<style>
  :root {
    --navy: #0a2d68;
    --navy-deep: #032459;
    --navy-light: #123f80;
    --ink: #1b1b1b;
    --text: #333333;
    --grey-band-top: #e4e4e4;
    --grey-band-bottom: #f6f6f6;
    --rule: #9a9a9a;
    --icon-grey: #b5b5b5;
    --white: #ffffff;
  }
  * { margin: 0; padding: 0; box-sizing: border-box; }
  html, body { width: 1200px; height: 888px; overflow: hidden; background: var(--white); }
  body { position: relative; font-family: "Arimo", Arial, sans-serif; color: var(--text); }

  .top-strip { position: absolute; left: 0; top: 0; width: 1200px; height: 5px; background: var(--navy); }
  .header-band {
    position: absolute; left: 0; top: 5px; width: 1200px; height: 137px;
    background: linear-gradient(180deg, var(--grey-band-top), var(--grey-band-bottom) 70%, var(--white));
  }

  .brand {
    position: absolute; left: 116px; top: 10px; width: 214px; height: 214px;
    border-radius: 50%; background: var(--navy);
    display: flex; align-items: center; justify-content: center; text-align: center;
    box-shadow: 0 0 0 5px var(--white), 0 0 0 7px #c9c9c9;
  }
  .brand-name {
    font-family: "Questrial", Arial, sans-serif; font-size: 21px; line-height: 1.25;
    color: var(--white); width: 160px; text-transform: uppercase; letter-spacing: 1px;
  }

  .client-login {
    position: absolute; left: 931px; top: 5px; width: 140px; height: 32px;
    background: var(--navy); border-radius: 0 0 3px 3px;
    display: flex; align-items: center; justify-content: center; gap: 7px;
    color: var(--white); font-size: 13px; font-weight: 700; text-decoration: none;
  }

  .header-social { position: absolute; left: 915px; top: 52px; display: flex; align-items: center; gap: 8px; }
  .header-social .dot { width: 20px; height: 20px; border-radius: 50%; background: var(--white); margin-right: 10px; }
  .header-social .icon { width: 32px; height: 32px; border-radius: 50%; background: var(--icon-grey); }

  .main-nav {
    position: absolute; left: 351px; top: 100px; width: 720px; height: 41px;
    border-top: 1px solid var(--rule); border-bottom: 1px solid #c8c8c8;
  }
  .main-nav a { position: absolute; top: 8px; font-size: 17px; color: var(--navy); text-decoration: none; }

  .side-social {
    position: absolute; left: 0; top: 288px; width: 52px; height: 180px;
    background: var(--white); border: 1px solid #bdbdbd; border-left: none;
    display: flex; flex-direction: column; align-items: center; justify-content: center; gap: 6px;
  }
  .side-social .icon { width: 26px; height: 26px; border-radius: 50%; background: var(--ink); display: flex; align-items: center; justify-content: center; }

  .hero-title {
    position: absolute; left: 152px; top: 280px;
    font-family: "Questrial", Arial, sans-serif; font-size: 58px; letter-spacing: 1px;
    color: transparent; -webkit-text-stroke: 1.6px var(--ink); line-height: 1;
    white-space: nowrap;
  }
  .hero-subtitle {
    position: absolute; left: 152px; top: 352px;
    font-family: "Questrial", Arial, sans-serif; font-size: 25px; color: #444; letter-spacing: 0.3px;
    white-space: nowrap;
  }
  .hero-text {
    position: absolute; left: 157px; top: 398px; width: 400px;
    font-size: 14.5px; line-height: 16px; color: var(--text);
  }

  .hero-visual {
    position: absolute; left: 644px; top: 213px; width: 457px; height: 427px;
    background: radial-gradient(ellipse at 50% 55%, #3a3a3a, #1a1a1a 45%, rgba(255,255,255,0) 72%);
  }

  .ground-line { position: absolute; left: 0; top: 739px; width: 1200px; height: 4px; background: #111; }

  .footer {
    position: absolute; left: 0; top: 743px; width: 1200px; height: 145px;
    background: linear-gradient(180deg, var(--navy-deep), var(--navy-light));
    color: var(--white);
  }
  .footer-nav { position: absolute; left: 124px; top: 25px; font-size: 15px; white-space: nowrap; }
  .footer-nav a { color: var(--white); text-decoration: none; }
  .footer-nav .sep { margin: 0 8px; }
  .copyright { position: absolute; left: 132px; top: 82px; font-size: 12.5px; line-height: 15px; }
  .contact { position: absolute; left: 911px; top: 25px; font-size: 12.5px; line-height: 14.5px; font-style: normal; }
  .contact h2 { font-size: 12.5px; font-weight: 400; margin-bottom: 14px; }
</style>
</head>
<body>
  <div class="top-strip"></div>
  <div class="header-band"></div>

  <div class="brand"><span class="brand-name">Law Office of Bernard T. Whitfield</span></div>

  <a class="client-login" href="#">
    <svg width="18" height="18" viewBox="0 0 18 18" aria-hidden="true">
      <circle cx="9" cy="9" r="8" fill="none" stroke="#fff" stroke-width="1.6"/>
      <path d="M9 4.5v9M4.5 9h9" stroke="#fff" stroke-width="2"/>
    </svg>
    CLIENT LOG-IN
  </a>

  <div class="header-social">
    <span class="dot"></span>
    <span class="icon"></span>
    <span class="icon"></span>
    <span class="icon"></span>
  </div>

  <nav class="main-nav">
    <a href="#" style="left:237px">Home</a>
    <a href="#" style="left:302px">About Us</a>
    <a href="#" style="left:390px">Our Services</a>
    <a href="#" style="left:505px">contact Us</a>
    <a href="#" style="left:602px">Legal Advisor</a>
  </nav>

  <div class="side-social">
    <span class="icon"></span>
    <span class="icon"></span>
    <span class="icon"></span>
    <span class="icon"></span>
    <span class="icon">
      <svg width="14" height="10" viewBox="0 0 14 10" aria-hidden="true">
        <rect x="0.5" y="0.5" width="13" height="9" fill="none" stroke="#fff"/>
        <path d="M0.5 0.5L7 6l6.5-5.5" fill="none" stroke="#fff"/>
      </svg>
    </span>
  </div>

  <h1 class="hero-title">LAW CENTER</h1>
  <p class="hero-subtitle">CENTRUM SPECJALISTÓW PRAWA</p>
  <p class="hero-text">Sed ut perspiciatis unde omnis iste natus error sit voluptatem accusantium doloremque laudantium, totam rem aperiam, eaque</p>

  <div class="hero-visual" role="img" aria-label="Black scales of justice with a judge's gavel"></div>

  <div class="ground-line"></div>

  <footer class="footer">
    <nav class="footer-nav">
      <a href="#">Home</a><span class="sep">|</span>
      <a href="#">About Us</a><span class="sep">|</span>
      <a href="#">Our Services</a><span class="sep">|</span>
      <a href="#">contact US</a><span class="sep">|</span>
      <a href="#">Legal Advisor</a>
    </nav>
    <p class="copyright">Copyright &nbsp;©2015 Law Office of Bernard T. Whitfield<br>All Right Reserved.</p>
    <address class="contact">
      <h2>CONTACT INFO:</h2>
      245 Harbor Lane<br>
      Road, D07 3120<br>
      Phone: +1 800 555 0142<br>
      EMAIL: info@rtvlegal.com
    </address>
  </footer>
</body>
</html>
```